Maple Lantern Business Card

Design of business cards

Target Market(s)

We are aiming as small business owners who need anything from basic business structures, website plans, business processes and quality assurance.

Industry/Entity Type

Business

Colors

Designer to choose colors to be used in the design.

Requirements
Nice to have
• I would prefer one side of the card to use the green from the logo. Prefer to have the same font as the logo.

```html
<!DOCTYPE html>
<html lang="en">
<head>
<meta charset="utf-8">
<title>Maple Lantern Consulting – Business Card</title>
<link rel="stylesheet" href="https://fonts.googleapis.com/css2?family=Gelasio:ital,wght@0,400;0,700;1,700&display=swap">
<style>
  :root {
    --brand-green: #a6ce39;
    --rule-green: #c9df8a;
    --ink-grey: #58595b;
    --ink-dark: #4a4a4a;
    --paper: #ffffff;
  }
  html, body {
    margin: 0;
    padding: 0;
    overflow: hidden;
    background: var(--paper);
  }
  .card {
    position: relative;
    width: 1200px;
    height: 741px;
    background: var(--brand-green);
    overflow: hidden;
    font-family: "Gelasio", Georgia, serif;
  }
  .card__panel {
    position: absolute;
    left: 0;
    top: 0;
    width: 808px;
    height: 587px;
    background: var(--paper);
  }
  .brand {
    position: absolute;
    left: 160px;
    top: 130px;
    display: flex;
    align-items: center;
    gap: 40px;
  }
  .brand__mark {
    width: 150px;
    height: 150px;
    background: var(--brand-green);
    flex: none;
  }
  .brand__name {
    margin: 0;
    color: var(--brand-green);
    font-weight: 700;
    font-size: 42px;
    line-height: 56px;
    font-variant: small-caps;
    letter-spacing: 1px;
  }
  .contact {
    position: absolute;
    left: 370px;
    top: 382px;
    height: 115px;
    padding-left: 22px;
    border-left: 2px solid var(--rule-green);
    color: var(--ink-grey);
  }
  .contact__name {
    margin: 12px 0 0;
    font-size: 35px;
    font-weight: 700;
    line-height: 44px;
  }
  .contact__phone {
    margin: 0;
    font-size: 36px;
    font-weight: 400;
    line-height: 48px;
  }
  .services {
    position: absolute;
    right: 73px;
    top: 656px;
    margin: 0;
    color: var(--ink-dark);
    font-size: 20.5px;
    font-style: italic;
    font-weight: 700;
  }
</style>
</head>
<body>
  <main class="card">
    <section class="card__panel">
      <div class="brand">
        <span class="brand__mark" aria-hidden="true"></span>
        <h1 class="brand__name">Maple<br>Lantern<br>Consulting</h1>
      </div>
      <div class="contact">
        <p class="contact__name">Marco Bellandri</p>
        <p class="contact__phone">555.014.2287</p>
      </div>
    </section>
    <p class="services">business structures, website plans, business processes &amp; quality assurance</p>
  </main>
</body>
</html>
```